Local Flower Farm Needs Business Card Design

I need business cards designed for a flower farm based in Eudora, Kansas.
Business Info:
We are a local cut flower farm located in Eudora, Kansas, founded by Darla Hoffstrom. What started as a passion for agriculture and search for more joy in daily life has blossomed into a small business dedicated to providing the community with beautiful, fresh, and sustainable flowers. We specialize in local, seasonal blooms, ensuring that every petal reflects the care and dedication we pour into our craft. Our mission is to deliver the highest quality flowers directly to our customers through local farmers markets and to florists who share our commitment to sustainability. Join us in celebrating the beauty of nature, one bloom at a time!
Contact Details:
Darla Hoffstrom
Owner
Phone 913-555-0147
Facebook: Lorabelle Quinn Blossoms
Instagram: @LorabelleQuinnBlossoms
Website: LorabelleQuinnBlossoms.example
Target Market(s)
Wholesale to Florists and Direct to Consumer via Farmers Market
Industry/Entity Type
Florist, Farm
Contact Information for Business Card
Name, Contact Info, Logo
Look and feel

```html
<!DOCTYPE html>
<html lang="en">
<head>
<meta charset="utf-8">
<title>Lorabelle Quinn Blossoms – Business Card</title>
<link rel="stylesheet" href="https://fonts.googleapis.com/css2?family=Libre+Baskerville&family=Outfit:wght@400&display=swap">
<style>
  :root {
    --ink: #0b2830;
    --paper: #ffffff;
    --backdrop: #9c9c9c;
    --serif: "Libre Baskerville", "Times New Roman", serif;
    --sans: "Outfit", "Helvetica Neue", sans-serif;
  }
  * { margin: 0; padding: 0; box-sizing: border-box; }
  html, body { width: 1093px; height: 1200px; overflow: hidden; }
  body { background: var(--backdrop); position: relative; font-family: var(--sans); }

  .card {
    position: absolute;
    left: 264px;
    width: 582px;
    height: 357px;
    border-radius: 24px;
    background: var(--ink);
    color: var(--paper);
    overflow: hidden;
  }
  .card--front { top: 226px; }
  .card--back { top: 621px; }

  /* Front: brand panel on the left */
  .brand-panel {
    position: absolute;
    left: 0; top: 0;
    width: 236px; height: 100%;
    background: var(--paper);
    border-radius: 0 90px 90px 0;
    display: flex;
    align-items: center;
    padding-left: 28px;
  }
  .brand-panel__name {
    font-family: var(--serif);
    font-size: 24px;
    line-height: 1.3;
    color: var(--ink);
  }

  .identity {
    position: absolute;
    right: 32px; top: 36px;
    text-align: right;
  }
  .identity__name {
    font-family: var(--serif);
    font-size: 20px;
    letter-spacing: 0.3px;
    text-transform: uppercase;
    line-height: 1.2;
  }
  .identity__title { font-size: 15px; line-height: 1.2; margin-top: 2px; }
  .identity__rule {
    position: absolute;
    right: 32px; top: 96px;
    width: 84px; height: 1px;
    background: var(--paper);
  }
  .identity__rule::before, .identity__rule::after {
    content: ""; position: absolute; top: -1.5px;
    width: 4px; height: 4px; border-radius: 50%; background: var(--paper);
  }
  .identity__rule::before { left: -1px; }
  .identity__rule::after { right: -1px; }

  .contacts {
    position: absolute;
    right: 24px; top: 209px;
    list-style: none;
  }
  .contacts__item {
    display: flex; justify-content: flex-end; align-items: center;
    gap: 5px; height: 26.3px;
    font-size: 16.5px;
  }
  .contacts__icon {
    width: 21px; height: 21px;
    border: 1px solid var(--paper);
    border-radius: 50%;
    display: flex; align-items: center; justify-content: center;
    flex: none;
  }
  .contacts__icon svg { width: 12px; height: 12px; }

  /* Back */
  .seal {
    position: absolute;
    left: 193px; top: 63px;
    width: 196px; height: 196px;
    border: 1px solid var(--paper);
    border-radius: 50%;
    display: flex; align-items: center; justify-content: center;
    text-align: center;
  }
  .seal__name {
    font-family: var(--serif);
    font-size: 19px;
    line-height: 1.35;
    text-transform: uppercase;
    letter-spacing: 1.5px;
  }
  .back-web {
    position: absolute;
    left: 0; right: 0; top: 300px;
    text-align: center;
    font-size: 17px;
    letter-spacing: 1.2px;
  }
</style>
</head>
<body>

<section class="card card--front">
  <div class="brand-panel">
    <p class="brand-panel__name">Lorabelle<br>Quinn<br>Blossoms</p>
  </div>

  <div class="identity">
    <h1 class="identity__name">Darla Hoffstrom</h1>
    <p class="identity__title">Owner</p>
  </div>
  <div class="identity__rule"></div>

  <ul class="contacts">
    <li class="contacts__item">913-555-0147
      <span class="contacts__icon">
        <svg viewBox="0 0 24 24" fill="none" stroke="#fff" stroke-width="2.2" stroke-linecap="round" stroke-linejoin="round"><path d="M5 3h4l2 5-2.5 1.5a11 11 0 0 0 6 6L16 13l5 2v4a2 2 0 0 1-2 2A16 16 0 0 1 3 5a2 2 0 0 1 2-2z"/></svg>
      </span>
    </li>
    <li class="contacts__item">Lorabelle Quinn Blossoms<span class="contacts__icon"></span></li>
    <li class="contacts__item">@LorabelleQuinnBlossoms<span class="contacts__icon"></span></li>
    <li class="contacts__item">LorabelleQuinnBlossoms.example
      <span class="contacts__icon">
        <svg viewBox="0 0 24 24" fill="none" stroke="#fff" stroke-width="1.8"><circle cx="12" cy="12" r="10"/><ellipse cx="12" cy="12" rx="4.5" ry="10"/><path d="M2 12h20M4 7h16M4 17h16"/></svg>
      </span>
    </li>
  </ul>
</section>

<section class="card card--back">
  <div class="seal">
    <p class="seal__name">Lorabelle<br>Quinn<br>Blossoms</p>
  </div>
  <p class="back-web">LorabelleQuinnBlossoms.example</p>
</section>

</body>
</html>
```